Birchline Septic Solutions

Would like to see some single sided ones but would also like to see some double sided with one sided only being the logo. Owners name is Tom Waldrick. Phone number is 555-214-8830
Services are pumping, inspections, installs, and repairs

Contact Information for Business Card

555-241-8830 Tom Waldrick Harrowvale, OH

```html
<!DOCTYPE html>
<html lang="en">
<head>
<meta charset="UTF-8">
<title>Birchline Septic Solutions – Business Card</title>
<link href="https://fonts.googleapis.com/css2?family=Montserrat:wght@400;500;700;800&display=swap" rel="stylesheet">
<style>
  :root {
    --teal: #07b8b2;
    --ink: #111111;
    --grey: #333333;
    --paper: #ffffff;
    --backdrop: #e9ecec;
  }
  * { box-sizing: border-box; margin: 0; padding: 0; }
  html, body { width: 1200px; height: 880px; overflow: hidden; }
  body {
    background: var(--backdrop);
    font-family: "Montserrat", sans-serif;
    display: flex;
    flex-direction: column;
    align-items: center;
    justify-content: center;
    gap: 40px;
  }
  .card {
    width: 660px;
    height: 377px;
    position: relative;
    overflow: hidden;
    box-shadow: 0 6px 18px rgba(0,0,0,0.18);
  }

  /* Logo side */
  .card--front {
    background: var(--teal);
    color: var(--paper);
    display: flex;
    flex-direction: column;
    align-items: center;
    justify-content: center;
    text-align: center;
  }
  .brand-name {
    font-weight: 800;
    font-size: 40px;
    letter-spacing: 3px;
    line-height: 1.1;
    text-transform: uppercase;
  }
  .brand-name--front { color: var(--paper); }
  .brand-name .line2 { display: block; font-size: 22px; letter-spacing: 7px; margin-top: 8px; }
  .services {
    margin-top: 34px;
    font-size: 19px;
    line-height: 1.45;
    font-weight: 500;
  }
  .tick {
    display: inline-block;
    width: 17px; height: 17px;
    vertical-align: -2px;
    margin: 0 5px;
  }

  /* Contact side */
  .card--back { background: var(--paper); }
  .wave { position: absolute; inset: 0; width: 100%; height: 100%; }
  .back-content {
    position: absolute;
    top: 58px; left: 60px;
    display: flex;
    align-items: center;
  }
  .brand-name--back { color: var(--ink); font-size: 30px; letter-spacing: 2px; }
  .brand-name--back .line2 { font-size: 16px; letter-spacing: 5px; color: var(--ink); }
  .divider {
    width: 2px; height: 120px;
    background: var(--teal);
    margin: 0 24px;
  }
  .contact-name {
    font-weight: 800;
    font-size: 22px;
    color: var(--ink);
    text-transform: uppercase;
  }
  .contact-name .surname { color: var(--teal); }
  .contact-role { font-size: 13px; color: var(--grey); margin: 2px 0 12px; }
  .contact-line {
    display: flex; align-items: center; gap: 8px;
    font-size: 14px; color: var(--ink); margin-top: 6px;
  }
  .contact-line svg { width: 14px; height: 14px; flex: none; }
</style>
</head>
<body>

  <section class="card card--front">
    <h1 class="brand-name brand-name--front">Birchline<span class="line2">Septic Solutions</span></h1>
    <p class="services">
      <svg class="tick" viewBox="0 0 20 20"><circle cx="10" cy="10" r="8.5" fill="none" stroke="#fff" stroke-width="2"/><path d="M6 10.5l3 3 5-6" fill="none" stroke="#fff" stroke-width="2"/></svg>Services are pumping
      <br>
      <svg class="tick" viewBox="0 0 20 20"><circle cx="10" cy="10" r="8.5" fill="none" stroke="#fff" stroke-width="2"/><path d="M6 10.5l3 3 5-6" fill="none" stroke="#fff" stroke-width="2"/></svg>inspections
      <svg class="tick" viewBox="0 0 20 20"><circle cx="10" cy="10" r="8.5" fill="none" stroke="#fff" stroke-width="2"/><path d="M6 10.5l3 3 5-6" fill="none" stroke="#fff" stroke-width="2"/></svg>installs
      <svg class="tick" viewBox="0 0 20 20"><circle cx="10" cy="10" r="8.5" fill="none" stroke="#fff" stroke-width="2"/><path d="M6 10.5l3 3 5-6" fill="none" stroke="#fff" stroke-width="2"/></svg>and repairs
    </p>
  </section>

  <section class="card card--back">
    <svg class="wave" viewBox="0 0 660 377" preserveAspectRatio="none" aria-hidden="true">
      <path d="M0 345 C220 325 400 290 485 222 C550 170 605 152 660 146 L660 377 L0 377 Z" fill="var(--teal)"/>
      <path d="M0 318 C210 300 380 266 478 210 C405 272 220 320 0 338 Z" fill="var(--ink)"/>
    </svg>
    <div class="back-content">
      <h2 class="brand-name brand-name--back">Birchline<span class="line2">Septic Solutions</span></h2>
      <div class="divider"></div>
      <div class="contact">
        <p class="contact-name">Tom <span class="surname">Waldrick</span></p>
        <p class="contact-role">Owners</p>
        <p class="contact-line">
          <svg viewBox="0 0 20 20"><path d="M2 8c0-3 3-5 8-5s8 2 8 5l-3 1-1-2H6L5 9 2 8zM4 10h12l1 7H3z" fill="var(--teal)"/></svg>
          555-214-8830
        </p>
        <p class="contact-line">
          <svg viewBox="0 0 20 20"><path d="M10 1a6 6 0 0 0-6 6c0 5 6 12 6 12s6-7 6-12a6 6 0 0 0-6-6zm0 8.5A2.5 2.5 0 1 1 10 4.5a2.5 2.5 0 0 1 0 5z" fill="var(--teal)"/></svg>
          Tom Waldrick Harrowvale, OH
        </p>
      </div>
    </div>
  </section>

</body>
</html>
```